Rapidly growing regional logistics company looking for a modern clean website design.

We need a website for a 5 year old company based in New England.
We offer a complete logistics solution. With services dedicated to the changing economic environment. Services to our customers include, same day delivery, trucking and van service, warehouse & storage, pool distribution, and B2B installations.
We've implemented leading technology along the way, that provides visibility, accountability, up to the minute tracking, and project management.
Our goal to be known in the industry we service as an excellent provider of time-critical services and dependability.
Independently of the services we offer, our customers know that they can count on a true partner.

Target Market(s)

B2B, including printers, retail, manufacturers, wholesalers, electronics, any company that needs product delivered or warehoused

Industry/Entity Type

Logistics

Coding

Coded - Design and coding required

Number of Pages Required

5+ page

Font styles to use
Sans Serif

Colors
0255a3

Requirements
Must have
• Clean, modern design, limited clutter. Limited tabs, preferred everything on 1st screen roll down to see info

```html
<!DOCTYPE html>
<html lang="en">
<head>
<meta charset="utf-8">
<title>Wexford Logistics</title>
<link href="https://fonts.googleapis.com/css2?family=Arimo:wght@400;700&display=swap" rel="stylesheet">
<style>
  :root {
    --brand-blue: #0255a3;
    --ink: #111111;
    --card-heading: #4d6884;
    --card-ink: #3b3b3b;
    --top-band: #7a0f12;
    --top-band-dark: #3a0506;
    --wood-light: #e3a46a;
    --wood-mid: #c9803f;
    --wood-dark: #a55e25;
    --card-fill: rgba(255, 255, 255, 0.38);
    --card-edge: rgba(255, 255, 255, 0.55);
  }
  * { margin: 0; padding: 0; box-sizing: border-box; }
  html, body {
    width: 1200px; height: 675px; overflow: hidden;
    background: #ffffff;
    font-family: "Arimo", Arial, sans-serif;
  }
  .page { position: relative; width: 1200px; height: 675px; }
  .top-band {
    height: 7px;
    background: linear-gradient(90deg, var(--top-band-dark), var(--top-band) 30%, var(--top-band-dark) 60%, var(--top-band) 85%, var(--top-band-dark));
  }
  .intro { padding: 0 15px; height: 473px; overflow: hidden; }
  .site-title {
    margin-top: 22px;
    text-align: center;
    color: var(--brand-blue);
    font-size: 28px;
    font-weight: 700;
    letter-spacing: 3.2px;
    line-height: 34px;
  }
  .intro p {
    color: var(--ink);
    font-size: 14px;
    line-height: 20.2px;
    text-align: justify;
    margin-top: 17px;
  }
  .intro p.lead { font-size: 15.4px; margin-top: 21px; line-height: 20px; letter-spacing: 0.2px; }
  .services {
    position: absolute; left: 0; top: 480px;
    width: 1200px; height: 195px;
    overflow: hidden;
    background: linear-gradient(120deg, var(--wood-mid) 0%, var(--wood-light) 25%, var(--wood-mid) 45%, var(--wood-light) 65%, var(--wood-dark) 85%, var(--wood-mid) 100%);
  }
  .service-card {
    position: absolute; top: 48px;
    width: 336px; height: 170px;
    background: var(--card-fill);
    border: 1px solid var(--card-edge);
    text-align: center;
    padding: 20px 22px 0;
  }
  .service-card:nth-child(1) { left: 48px; }
  .service-card:nth-child(2) { left: 432px; }
  .service-card:nth-child(3) { left: 816px; }
  .service-card h2 {
    color: var(--card-heading);
    font-size: 19px;
    font-weight: 700;
    letter-spacing: 1.2px;
    line-height: 24px;
  }
  .service-card p {
    margin-top: 12px;
    color: var(--card-ink);
    font-size: 13.5px;
    line-height: 20.5px;
  }
</style>
</head>
<body>
<div class="page">
  <div class="top-band" role="img" aria-label="Header photograph strip"></div>
  <main class="intro">
    <h1 class="site-title">WELCOME TO WEXFORD LOGISTICS HOMEPAGE</h1>
    <p class="lead">Wexford Logistics is a Logistics Company dedicated to serving you as soon as you require our services in addition to offering the best customer care attendance in the market to your Total Satisfaction</p>
    <p>Founded five years ago in New England, Wexford Logistics offers a complete logistics solution built around the changing economic environment. Our services include same day delivery, trucking and van service, warehouse and storage, pool distribution and B2B installations for printers, retailers, manufacturers, wholesalers, electronics firms and any business that needs product delivered or warehoused. Every shipment is backed by leading technology that gives you full visibility, clear accountability, up to the minute tracking and hands-on project management from pickup to final signature. Our dispatch team watches each route in real time, so changes in schedule, weather or volume are handled before they become delays. Whether you need a single rush package across town or a recurring freight lane across the region, we scale our fleet and our warehouse space to match your demand, keeping costs predictable and deliveries on time. From the first quote to the final proof of delivery, one dedicated account contact keeps every detail in hand.</p>
    <p>Our goal is to be known across the industries we serve as an excellent provider of time-critical services and dependability. Same day and scheduled runs are covered by our own trucks and vans, driven by trained staff who treat your freight as carefully as you would. Secure warehouse space lets you store inventory close to your customers, while pool distribution consolidates shipments to cut transit times and lower the cost per stop. Our B2B installation crews deliver, unpack, place and set up equipment on site, then remove all packaging so your team can get straight back to work.</p>
    <p>Independently of the services we offer, our customers know that they can count on a true partner. Our online portal shows live shipment status, signed proof of delivery and inventory levels at any hour, and clear reports help you plan ahead with confidence. When plans change, a real person answers the phone and finds a solution, not an excuse. Tell us what you need to move or store, and we will build a logistics plan that fits your business today and keeps growing with you tomorrow as your volume, your customers and your reach expand across the region.</p>
  </main>
  <section class="services" role="img" aria-label="Background photograph of a parquet wooden floor">
    <article class="service-card">
      <h2>SAME DAY DELIVERY</h2>
      <p>Urgent freight picked up and delivered within hours by our own trucks and vans, with live tracking and signed proof of delivery on every run across the region.</p>
    </article>
    <article class="service-card">
      <h2>WAREHOUSE &amp; STORAGE</h2>
      <p>Secure, flexible space close to your customers, with real-time inventory counts, pick and pack, and pool distribution that lowers the cost of every stop.</p>
    </article>
    <article class="service-card">
      <h2>B2B INSTALLATIONS</h2>
      <p>Trained crews deliver, unpack, place and set up your equipment on site, then remove the packaging so your team can get straight back to business.</p>
    </article>
  </section>
</div>
</body>
</html>
```